FIELDLINE MENTORS Flyer Design

I need a flyer designed with information about our company and what all we offer.

Fieldline Mentors Inc
Website: www.FIELDLINEMentors.example
Email Address: Info@FIELDLINEMentors.example

Who We Are
Fieldline Mentors is a social networking site tailored initially for coaches looking to connect with other coaches and further their careers in the coaching industry. With the social networking environment rapidly growing everyday, we believe other networks will eventually want to be apart of Fieldline Mentors. Using our current network, resources, and innovation we believe Fieldline Mentors has the potential to help many coaches from around the nation further their careers which is a win/win for all involved parties.

What We Sell
Fieldline Mentors will sell monthly memberships to our members, as well as advertising space to vendors related to the sports industry and other industries. Our main emphasis will be on providing value-add content for our members, but will also focus on securing exclusive partnerships with various vendors to provide discounts to our premium members.

Who We Sell To
Our primary target market is the 850,000 coaches in the United States.

MEMBER BENEFITS
Gain exclusive access to coaches from around the country. When you sign up for a Year Membership you are automatically enrolled in the FIELDLINE KORVAL REWARDS Program. This EXCLUSIVE Rewards Program is about giving our members access to exclusive discounts at over 300,000 retailers and vendors we have partnered with around the nation. Our password-protected web portal offers access to national and local savings as well as a turnkey mobile coupon app developed for both Quince QOS and Velorix mobile platforms.

On the Back of it I would like to include information about our Rewards Program which is below. It doesn't have to include all of it. To learn more information about the Program they can visit www.KORVAL.example/Rewards

Dining Discounts
Enjoy savings of up to 50% off at over 70,000 dining locations nationwide, including fine restaurants, casual dining, fast food, desserts, catering, take-out, delivery and more.

Hotel Program
Members enjoy savings at luxury resorts, business and leisure hotels, and even economy motels. You’ll always rest easy with discounts on the best available rates at over 31,000 name-brand hotels worldwide. Hotel properties include Brackley, Tall Meadow, Pelican Hotels and most popular national brands.

Recreation & Entertainment Access
Members save up to 50% at nearly 20,000 locations like popular theme parks, professional sporting events, theater productions, bowling alleys, laser tag, white-water rafting, museums, arcades, high-adventure excursions, cultural events and much more.

Travel Package Savings
Members can pack their bags with savings—up to 50% off—on travel packages worldwide with preferred rates from national travel agencies on all-inclusive vacations.

Car Rentals
Consistently among our most popular categories, as members enjoy exclusive deals at the most prominent car rental companies. Members enjoy free upgrades, free days, and other exclusive offers for any travel season.

Automotive Discounts
KORVAL Reward members will save on everything from oil changes and tune-ups to major repairs and body work. Buckle up and save at nearly 40,000 locations nationwide.

Shopping Discounts
From apparel, electronics, home décor, department stores, furniture, appliances, and even groceries, your members will save up to 50% on the things they buy every day at over 35,000 locations—both in-store and online.

Household Services
Members save on cell phones and service, cable/satellite TV, tax services, financial services, dry cleaning, moving & storage, internet service, and more—at over 45,000 locations.

VIP Events
As Exclusive Member of KORVAL Rewards Program you gain access to tickets to events such as ZRT Awards in Nashville, Grand Pennant Games, Marlow Stakes, UCAB Championship Games, and many other Bucket List Events.

Industry/Entity Type

It Company

```html
<!DOCTYPE html>
<html lang="en">
<head>
<meta charset="utf-8">
<title>Fieldline Mentors Flyer</title>
<link rel="stylesheet" href="https://fonts.googleapis.com/css2?family=Lato:wght@400;700;900&display=swap">
<style>
  :root {
    --red: #e3141b;
    --ink: #161616;
    --charcoal: #2a2a2a;
    --paper: #ffffff;
    --backdrop: #e6e6e6;
    --photo-light: #e2e2e2;
    --photo-dark: #8d8d8d;
  }
  * { box-sizing: border-box; margin: 0; padding: 0; }
  html, body { width: 1200px; height: 805px; overflow: hidden; }
  body {
    background: var(--backdrop);
    font-family: 'Lato', sans-serif;
    position: relative;
  }
  .flyer {
    position: absolute;
    top: 62px;
    width: 520px;
    height: 670px;
    background: var(--paper);
    overflow: hidden;
    box-shadow: 0 4px 14px rgba(0,0,0,.25);
  }
  .flyer--front { left: 60px; }
  .flyer--back { left: 620px; }
  .shapes { position: absolute; inset: 0; width: 100%; height: 100%; }

  /* Front */
  .hero-photo {
    position: absolute; left: 0; top: 150px; width: 520px; height: 270px;
    background: linear-gradient(160deg, var(--photo-light), var(--photo-dark));
  }
  .intro-box {
    position: absolute; left: 6px; top: -4px; width: 268px; height: 220px;
    background: var(--red); border-radius: 8px; padding: 14px 10px 8px;
    color: var(--paper);
  }
  .intro-box h2 {
    font-weight: 900; font-size: 22px; color: var(--ink); margin-bottom: 8px;
  }
  .intro-box p { font-size: 11.3px; line-height: 1.2; text-align: justify; hyphens: auto; }
  .brand-name {
    position: absolute; left: 282px; top: 20px; width: 232px;
    font-size: 21px; font-weight: 700; color: var(--red);
    text-align: center; letter-spacing: .3px;
  }
  .details {
    position: absolute; right: 14px; top: 334px; width: 318px;
    color: var(--paper); text-align: right;
  }
  .details h3 {
    color: var(--red); font-size: 11.5px; line-height: 14px; font-weight: 900;
    text-transform: uppercase; margin: 10px 0 5px;
  }
  .details h3:first-child { margin-top: 0; }
  .details p {
    font-size: 10.3px; line-height: 1.3;
    text-align: justify; text-align-last: right; hyphens: auto;
  }
  .contacts {
    position: absolute; left: 12px; top: 512px; list-style: none;
    color: var(--paper); font-size: 7.6px; font-weight: 900;
  }
  .contacts li { display: flex; align-items: center; gap: 6px; margin-bottom: 16px; }
  .contacts svg { width: 11px; height: 11px; flex: none; }

  /* Back */
  .title-bar {
    position: absolute; left: 0; background: var(--red);
    font-weight: 900; color: var(--ink); font-size: 38px; line-height: 40px;
    padding: 0 8px 0 20px;
  }
  .title-bar--one { top: 24px; }
  .title-bar--two { top: 70px; }
  .strategy-photo {
    position: absolute; right: 0; top: 0; width: 170px; height: 110px;
    background: linear-gradient(135deg, #f4f4f4, #9a9a9a);
  }
  .benefits {
    position: absolute; right: 12px; top: 158px; width: 495px;
    color: var(--paper); text-align: right;
  }
  .benefit h3 {
    display: inline-block; background: var(--paper); color: var(--red);
    font-size: 19px; font-weight: 900; text-transform: uppercase;
    padding: 1px 12px 1px 16px; border-radius: 14px 0 0 14px;
    margin-right: -12px; margin-bottom: 8px; line-height: 22px;
  }
  .benefit p {
    font-size: 12px; line-height: 1.22; margin-bottom: 12px;
    text-align: justify; text-align-last: right; hyphens: auto;
  }
  .benefit--dining p { width: 430px; margin-left: auto; text-align: right; }
  .call-out {
    position: absolute; left: 0; top: 560px; width: 520px; height: 76px;
    background: var(--red); color: var(--paper); text-align: center;
    font-weight: 900; font-size: 13.5px; line-height: 1.35; padding-top: 18px;
  }
</style>
</head>
<body>

<section class="flyer flyer--front">
  <div class="hero-photo" role="img" aria-label="Photo of a keyboard key labelled Coaching with a rising chart icon"></div>
  <svg class="shapes" viewBox="0 0 520 670" aria-hidden="true">
    <path d="M0 0H520V130C380 150 200 200 0 262Z" fill="#fff"/>
    <path d="M0 262C200 200 380 150 520 130V152C380 170 200 220 0 292Z" fill="#2a2a2a"/>
    <defs>
      <linearGradient id="frontDark" x1="0" y1="0" x2="0" y2="1">
        <stop offset="0" stop-color="#4a4a4a"/>
        <stop offset="1" stop-color="#1e1e1e"/>
      </linearGradient>
    </defs>
    <path d="M0 468C160 395 340 345 520 330V670H0Z" fill="url(#frontDark)"/>
    <path d="M0 448C160 375 340 330 520 318V330C340 345 160 395 0 482Z" fill="#e3141b"/>
    <rect x="0" y="654" width="520" height="16" fill="#e3141b"/>
  </svg>

  <div class="intro-box">
    <h2>WHO WE ARE</h2>
    <p>Fieldline Mentors is a social networking site tailored initially for coaches looking to connect with other coaches and further their careers in the coaching industry. With the social networking environment rapidly growing everyday, we believe other networks will eventually want to be apart of Fieldline Mentors. Using our current network, resources, and innovation we believe Fieldline Mentors has the potential to help many coaches from around the nation further their careers which is a win/win for all involved parties.</p>
  </div>

  <div class="brand-name">FIELDLINE MENTORS</div>

  <div class="details">
    <h3>What We Sell</h3>
    <p>Fieldline Mentors will sell monthly memberships to our members, as well as advertising space to vendors related to the sports industry and other industries. Our main emphasis will be on providing value-add content for our members, but will also focus on securing exclusive partnerships with various vendors to provide discounts to our premium members.</p>
    <h3>Who We Sell To</h3>
    <p>Our primary target market is the 850,000 coaches in the United States.</p>
    <h3>Member Benefits</h3>
    <p>Gain exclusive access to coaches from around the country. When you sign up for a Year Membership you are automatically enrolled in the FIELDLINE KORVAL REWARDS Program. This EXCLUSIVE Rewards Program is about giving our members access to exclusive discounts at over 300,000 retailers and vendors we have partnered with around the nation. Our password-protected web portal offers access to national and local savings as well as a turnkey mobile coupon app developed for both Quince QOS and Velorix mobile platforms.</p>
  </div>

  <ul class="contacts">
    <li>
      <svg viewBox="0 0 14 14"><circle cx="7" cy="7" r="6" fill="none" stroke="#e3141b" stroke-width="1.5"/><ellipse cx="7" cy="7" rx="2.6" ry="6" fill="none" stroke="#e3141b" stroke-width="1.2"/><line x1="1" y1="7" x2="13" y2="7" stroke="#e3141b" stroke-width="1.2"/></svg>
      WWW.FIELDLINEMENTORS.EXAMPLE
    </li>
    <li>
      <svg viewBox="0 0 14 14"><rect x="1" y="3" width="12" height="8" rx="1" fill="#e3141b"/><path d="M1.5 3.5L7 8l5.5-4.5" fill="none" stroke="#2a2a2a" stroke-width="1"/></svg>
      INFO@FIELDLINEMENTORS.EXAMPLE
    </li>
  </ul>
</section>

<section class="flyer flyer--back">
  <div class="strategy-photo" role="img" aria-label="Photo of a businessman drawing a leadership diagram with words like Motivate, Inspire, Coach and Vision"></div>
  <svg class="shapes" viewBox="0 0 520 670" aria-hidden="true">
    <defs>
      <linearGradient id="backDark" x1="0" y1="0" x2="0" y2="1">
        <stop offset="0" stop-color="#505050"/>
        <stop offset="1" stop-color="#1e1e1e"/>
      </linearGradient>
    </defs>
    <path d="M0 250C140 170 320 138 520 130V670H0Z" fill="url(#backDark)"/>
    <path d="M0 232C140 154 320 124 520 118V130C320 138 140 170 0 250Z" fill="#e3141b"/>
  </svg>

  <div class="title-bar title-bar--one">OUR REWARDS</div>
  <div class="title-bar title-bar--two">PROGRAM</div>

  <div class="benefits">
    <article class="benefit benefit--dining">
      <h3>Dining Discounts</h3>
      <p>Enjoy savings of up to 50% off at over 70,000 dining locations nationwide, including fine restaurants, casual dining, fast food, desserts, catering, take-out, delivery and more.</p>
    </article>
    <article class="benefit">
      <h3>Hotel Program</h3>
      <p>Members enjoy savings at luxury resorts, business and leisure hotels, and even economy motels. You’ll always rest easy with discounts on the best available rates at over 31,000 name-brand hotels worldwide. Hotel properties include Brackley, Tall Meadow, Pelican Hotels and most popular national brands.</p>
    </article>
    <article class="benefit">
      <h3>Recreation &amp; Entertainment Access</h3>
      <p>Members save up to 50% at nearly 20,000 locations like popular theme parks, professional sporting events, theater productions, bowling alleys, laser tag, white-water rafting, museums, arcades, high-adventure excursions, cultural events and much more.</p>
    </article>
    <article class="benefit">
      <h3>Travel Package Savings</h3>
      <p>Members can pack their bags with savings—up to 50% off—on travel packages worldwide with preferred rates from national travel agencies on all-inclusive vacations</p>
    </article>
  </div>

  <div class="call-out">
    TO LEARN MORE INFORMATION ABOUT THE PROGRAM YOU CAN VISIT<br>
    WWW.KORVAL.EXAMPLE/REWARDS
  </div>
</section>

</body>
</html>
```